Book Cover Design - "Walruses Seldom Whistle"

Looking for an eye-catching but professional book cover.

This book is designed to help people figure out why they hate their job and what to do about it.

The audience for this book is 18-35 year olds who feel stuck in their current roles. The theory here is that people often wind up in a job they don't love, then settle because they don't realize they can make things better.

The writer's style is clever and balances humor with practical advice.

```html
<!DOCTYPE html>
<html lang="en">
<head>
<meta charset="utf-8">
<title>Walruses Seldom Whistle – Book Cover</title>
<link rel="stylesheet" href="https://fonts.googleapis.com/css2?family=Anton&family=Courier+Prime&display=swap">
<style>
  :root {
    --night: #051720;
    --band: #231f20;
    --glow-top: #ffe92b;
    --glow-bottom: #f47c20;
    --byline: #ffffff;
  }
  html, body {
    margin: 0;
    padding: 0;
    width: 804px;
    height: 1200px;
    overflow: hidden;
    background: var(--night);
  }
  .cover {
    position: relative;
    width: 804px;
    height: 1200px;
    overflow: hidden;
    background: var(--night);
  }
  .cover-svg {
    position: absolute;
    left: 0;
    top: 0;
    width: 804px;
    height: 1200px;
    display: block;
  }
  .title-line {
    font-family: "Anton", "Impact", sans-serif;
    font-size: 222px;
    text-transform: uppercase;
    fill: url(#glow);
  }
  .figure { fill: url(#glow-box); }
  .band { fill: var(--band); }
  .byline {
    font-family: "Courier Prime", "Courier New", monospace;
    font-size: 21px;
    fill: var(--byline);
  }
  .glow-top { stop-color: var(--glow-top); }
  .glow-bottom { stop-color: var(--glow-bottom); }
</style>
</head>
<body>
<main class="cover">
  <svg class="cover-svg" viewBox="0 0 804 1200" aria-labelledby="cover-title">
    <title id="cover-title">Walruses Seldom Whistle, by writer name</title>
    <defs>
      <linearGradient id="glow" x1="0" y1="0" x2="0" y2="1">
        <stop offset="0.25" class="glow-top"/>
        <stop offset="1" class="glow-bottom"/>
      </linearGradient>
      <linearGradient id="glow-box" x1="0" y1="0" x2="0" y2="1">
        <stop offset="0" class="glow-top"/>
        <stop offset="1" class="glow-bottom"/>
      </linearGradient>
    </defs>

    <g class="cover-art" role="img" aria-label="Silhouettes of a man holding hands with one woman while offering a rose to another woman">
      <rect class="figure" x="144" y="192" width="100" height="350" rx="40"/>
      <rect class="figure" x="300" y="180" width="124" height="352" rx="40"/>
      <rect class="figure" x="610" y="190" width="96" height="336" rx="40"/>
    </g>

    <g class="title">
      <text class="title-line" x="10" y="744" textLength="788" lengthAdjust="spacingAndGlyphs">Walruses</text>
      <text class="title-line" x="0" y="984" textLength="804" lengthAdjust="spacingAndGlyphs">Seldom</text>
      <text class="title-line" x="8" y="1198" textLength="792" lengthAdjust="spacingAndGlyphs">Whistle</text>
    </g>

    <g class="author-band">
      <polygon class="band" points="0,840 804,794 804,886 0,934"/>
      <text class="byline" x="403" y="871" text-anchor="middle" transform="rotate(-3.3 403 864)">by writer name</text>
    </g>
  </svg>
</main>
</body>
</html>
```